Poster for List of Company Values

We need a poster to outline our Values which will be displayed in our office as well as posted on our website and other platforms (so need to allow for some flexibly in its application).

File attached outlines what we currently have with design and also our company style guide.

Note that we are looking for a modern, clean look, which still represents our core activities of construction and environmental services.

You can also reference our website here:

https://quorvelgroup.com.au/

Happy to answer any questions you might have.

Thanks for your interest,
Brent

Target Market(s)

Internal and External clients

Industry/Entity Type

Construction, water and recycling

Font styles to use
Sans Serif

Requirements
Must have
• All values on the one page. Graphic to represent each value. Also needs to use company logo
Nice to have
• Preference for poster to be orientated in landscape
Should not have
• Do not follow example provided, this is only to demonstrate what we have to date and also the text required

```html
<!DOCTYPE html>
<html lang="en">
<head>
<meta charset="utf-8">
<title>Quorvel Group – Our Values</title>
<link rel="stylesheet" href="https://fonts.googleapis.com/css2?family=Bebas+Neue&family=Montserrat:wght@400;700;800&display=swap">
<style>
  :root {
    --stage: #bdbec0;
    --paper: #ffffff;
    --navy: #1c3a8c;
    --field: #24479a;
    --green: #3fae49;
    --ink: #333333;
    --white: #ffffff;
  }
  * { margin: 0; padding: 0; box-sizing: border-box; }
  html, body { width: 690px; height: 1200px; overflow: hidden; }
  body { background: var(--stage); }
  .sheet { display: block; width: 690px; height: 1200px; }

  .paper { fill: var(--paper); }
  .field { fill: var(--field); }
  .brand-name { font-family: "Montserrat", sans-serif; font-weight: 700; font-size: 34px; fill: var(--ink); text-anchor: middle; }
  .headline { font-family: "Bebas Neue", sans-serif; font-size: 52px; text-anchor: end; }
  .headline .green { fill: var(--green); }
  .headline .navy { fill: var(--navy); }

  .frame { fill: none; stroke: var(--green); stroke-width: 5; stroke-linejoin: miter; }

  .value-title { font-family: "Montserrat", sans-serif; font-weight: 800; font-size: 21px; fill: var(--green); }
  .value-text { font-family: "Montserrat", sans-serif; font-weight: 400; font-size: 13px; fill: var(--white); }
  .value-kicker { font-family: "Montserrat", sans-serif; font-weight: 700; font-size: 13px; fill: var(--white); }
  .landscape .value-title { font-size: 18.5px; }
  .landscape .value-text, .landscape .value-kicker { font-size: 11.8px; }

  .icon-white { fill: none; stroke: var(--white); stroke-width: 4; stroke-linecap: round; stroke-linejoin: round; }
  .icon-green { fill: none; stroke: var(--green); stroke-width: 4; stroke-linecap: round; stroke-linejoin: round; }
</style>
</head>
<body>
<svg class="sheet" viewBox="0 0 1456 2533" preserveAspectRatio="none" xmlns="http://www.w3.org/2000/svg">
  <defs>
    <linearGradient id="site-tone" x1="0" y1="0" x2="0" y2="1">
      <stop offset="0" stop-color="#2a4c9f"/>
      <stop offset="0.5" stop-color="#24479a"/>
      <stop offset="1" stop-color="#213f90"/>
    </linearGradient>
    <g id="icon-flag" class="icon-white">
      <path d="M-40 -45 L-40 45"/>
      <path d="M-40 -45 L10 -45 L0 -28 L10 -10 L-40 -10"/>
      <rect x="-55" y="10" width="40" height="30" rx="6"/>
      <rect x="10" y="5" width="42" height="40"/>
      <path d="M-15 25 L10 25"/>
    </g>
    <g id="icon-hands" class="icon-green">
      <path d="M-55 -5 L-30 -30 L0 -15 L30 -30 L55 -5 L25 30 L0 40 L-25 30 Z"/>
      <path d="M-10 -20 L15 5 M0 5 L20 22 M-15 15 L5 32"/>
    </g>
    <g id="icon-bulb" class="icon-white">
      <circle cx="0" cy="-10" r="28"/>
      <path d="M-12 18 L-12 35 L12 35 L12 18"/>
      <path d="M-10 44 L10 44"/>
      <path d="M-45 -45 L-35 -35 M45 -45 L35 -35 M0 -52 L0 -44"/>
    </g>
    <g id="icon-heart-green" class="icon-green">
      <path d="M0 45 L-45 0 C-65 -25 -40 -55 -15 -40 L0 -28 L15 -40 C40 -55 65 -25 45 0 Z"/>
      <path d="M-25 5 L0 -15 L25 10 M-10 15 L10 30"/>
    </g>
    <g id="icon-heart-white" class="icon-white">
      <path d="M0 45 L-45 0 C-65 -25 -40 -55 -15 -40 L0 -28 L15 -40 C40 -55 65 -25 45 0 Z"/>
      <path d="M-30 35 L-10 10 L10 -15 M-15 40 L15 5"/>
    </g>
    <g id="icon-shield" class="icon-green">
      <path d="M-42 -48 L42 -48 L42 10 C42 35 20 48 0 48 C-20 48 -42 35 -42 10 Z"/>
      <path d="M-42 -5 L42 -5"/>
      <path d="M-6 5 L6 5 L6 17 L18 17 L18 29 L6 29 L6 41 L-6 41 L-6 29 L-18 29 L-18 17 L-6 17 Z"/>
    </g>
  </defs>

  <!-- Portrait poster -->
  <g class="portrait">
    <rect class="field" x="346" y="158" width="764" height="1180"/>
    <rect x="346" y="374" width="764" height="964" fill="url(#site-tone)" role="img" aria-label="Blue-toned photograph of construction workers on site in front of a city skyline"/>
    <rect class="paper" x="346" y="158" width="764" height="216"/>
    <text class="brand-name" x="455" y="308">QUORVEL</text>
    <text class="brand-name" x="455" y="340">Group</text>
    <g class="headline">
      <text class="green" x="1081" y="217" textLength="170" lengthAdjust="spacingAndGlyphs">INNOVATORS</text>
      <text class="navy" x="1081" y="259" textLength="234" lengthAdjust="spacingAndGlyphs">INCONSTRUCTION</text>
      <text class="green" x="1081" y="302" textLength="273" lengthAdjust="spacingAndGlyphs">AND ENVIROMENTAL</text>
      <text class="navy" x="1081" y="344" textLength="193" lengthAdjust="spacingAndGlyphs">MANAGEMENT</text>
    </g>
    <path class="frame" d="M585 424 L483 424 L448 497 L483 568 L980 568 L1008 637 L980 710 L483 710 L448 782 L483 853 L980 853 L1008 924 L980 996 L483 996 L448 1068 L483 1139 L980 1139 L1008 1210 L980 1282 L730 1282"/>

    <use href="#icon-flag" x="905" y="490" role="img" aria-label="Icon: hand holding a flag"/>
    <use href="#icon-hands" x="905" y="636" role="img" aria-label="Icon: handshake"/>
    <use href="#icon-bulb" x="905" y="782" role="img" aria-label="Icon: team idea"/>
    <use href="#icon-heart-green" x="905" y="924" role="img" aria-label="Icon: handshake in a heart"/>
    <use href="#icon-heart-white" x="905" y="1066" role="img" aria-label="Icon: open hands over a heart"/>
    <use href="#icon-shield" x="905" y="1210" role="img" aria-label="Icon: be positive badge with a plus sign"/>

    <text class="value-title" x="504" y="467">SHOW</text>
    <text class="value-title" x="504" y="486">INITIATIVE</text>
    <text class="value-text" x="504" y="503">We celebrate and recognize</text>
    <text class="value-text" x="504" y="517">our own and encourage</text>
    <text class="value-text" x="504" y="530">forward thinking.</text>

    <text class="value-title" x="504" y="612">BE</text>
    <text class="value-title" x="504" y="631">LOYAL</text>
    <text class="value-text" x="504" y="648">We take care of our own and</text>
    <text class="value-text" x="504" y="661">provide opportunities to listen</text>
    <text class="value-text" x="504" y="675">and support each other.</text>

    <text class="value-title" x="503" y="746">THINK</text>
    <text class="value-title" x="503" y="765">TEAM</text>
    <text class="value-text" x="503" y="782">We communicate</text>
    <text class="value-text" x="503" y="795">effectively and work as a</text>
    <text class="value-text" x="503" y="809">team by helping and</text>
    <text class="value-text" x="503" y="822">supporting each other.</text>

    <text class="value-title" x="503" y="902">SHOW</text>
    <text class="value-title" x="503" y="921">RESPECT</text>
    <text class="value-text" x="503" y="941">We value the diversity</text>
    <text class="value-text" x="503" y="954">and opinions of all.</text>

    <text class="value-title" x="503" y="1029">BE OPEN</text>
    <text class="value-title" x="503" y="1048">AND HONEST</text>
    <text class="value-text" x="503" y="1065">We are clear and open</text>
    <text class="value-text" x="503" y="1078">with each other, and</text>
    <text class="value-text" x="503" y="1091">provide an approachable</text>
    <text class="value-text" x="503" y="1104">and friendly</text>
    <text class="value-text" x="503" y="1118">environment.</text>

    <text class="value-title" x="503" y="1175">BE</text>
    <text class="value-title" x="503" y="1193">POSITIVE</text>
    <text class="value-kicker" x="503" y="1208">SMILE</text>
    <text class="value-text" x="503" y="1221">We are solutions focused and</text>
    <text class="value-text" x="503" y="1235">encourage a positive attitude</text>
    <text class="value-text" x="503" y="1248">turning a negative into a</text>
    <text class="value-text" x="503" y="1261">positive.</text>
  </g>

  <!-- Landscape poster -->
  <g class="landscape">
    <rect class="field" x="137" y="1549" width="1181" height="764"/>
    <rect x="137" y="1777" width="1181" height="536" fill="url(#site-tone)" role="img" aria-label="Blue-toned photograph of construction workers on site"/>
    <rect class="paper" x="137" y="1549" width="1181" height="228"/>
    <text class="brand-name" x="283" y="1711">QUORVEL</text>
    <text class="brand-name" x="283" y="1742">Group</text>
    <g class="headline">
      <text class="green" x="1264" y="1620" textLength="170" lengthAdjust="spacingAndGlyphs">INNOVATORS</text>
      <text class="navy" x="1264" y="1662" textLength="233" lengthAdjust="spacingAndGlyphs">INCONSTRUCTION</text>
      <text class="green" x="1264" y="1705" textLength="274" lengthAdjust="spacingAndGlyphs">AND ENVIROMENTAL</text>
      <text class="navy" x="1264" y="1747" textLength="193" lengthAdjust="spacingAndGlyphs">MANAGEMENT</text>
    </g>
    <path class="frame" d="M675 1860 L215 1860 L187 1925 L215 1990 L675 1990 L703 2057 L675 2122 L215 2122 L187 2188 L215 2255 L675 2255"/>
    <path class="frame" d="M1242 1860 L782 1860 L752 1925 L782 1990 L1242 1990 L1270 2057 L1242 2122 L782 2122 L752 2188 L782 2255 L1242 2255"/>

    <g transform="translate(600 1920) scale(0.92)"><use href="#icon-flag" role="img" aria-label="Icon: hand holding a flag"/></g>
    <g transform="translate(600 2055) scale(0.92)"><use href="#icon-hands" role="img" aria-label="Icon: handshake"/></g>
    <g transform="translate(600 2190) scale(0.92)"><use href="#icon-bulb" role="img" aria-label="Icon: team idea"/></g>
    <g transform="translate(1183 1920) scale(0.92)"><use href="#icon-heart-green" role="img" aria-label="Icon: handshake in a heart"/></g>
    <g transform="translate(1183 2055) scale(0.92)"><use href="#icon-heart-white" role="img" aria-label="Icon: open hands over a heart"/></g>
    <g transform="translate(1183 2190) scale(0.92)"><use href="#icon-shield" role="img" aria-label="Icon: be positive badge with a plus sign"/></g>

    <text class="value-title" x="233" y="1898">SHOW</text>
    <text class="value-title" x="233" y="1915">INITIATIVE</text>
    <text class="value-text" x="233" y="1932">We celebrate and recognize</text>
    <text class="value-text" x="233" y="1944">our own and encourage</text>
    <text class="value-text" x="233" y="1957">forward thinking.</text>

    <text class="value-title" x="233" y="2030">BE</text>
    <text class="value-title" x="233" y="2047">LOYAL</text>
    <text class="value-text" x="233" y="2065">We take care of our own and</text>
    <text class="value-text" x="233" y="2077">provide opportunities to listen</text>
    <text class="value-text" x="233" y="2090">and support each other.</text>

    <text class="value-title" x="232" y="2155">THINK</text>
    <text class="value-title" x="232" y="2172">TEAM</text>
    <text class="value-text" x="232" y="2189">We communicate</text>
    <text class="value-text" x="232" y="2201">effectively and work as a</text>
    <text class="value-text" x="232" y="2214">team by helping and</text>
    <text class="value-text" x="232" y="2226">supporting each other.</text>

    <text class="value-title" x="812" y="1903">SHOW</text>
    <text class="value-title" x="812" y="1920">RESPECT</text>
    <text class="value-text" x="812" y="1940">We value the diversity</text>
    <text class="value-text" x="812" y="1952">and opinions of all.</text>

    <text class="value-title" x="812" y="2020">BE OPEN</text>
    <text class="value-title" x="812" y="2037">AND HONEST</text>
    <text class="value-text" x="812" y="2054">We are clear and open</text>
    <text class="value-text" x="812" y="2066">with each other, and</text>
    <text class="value-text" x="812" y="2079">provide an approachable</text>
    <text class="value-text" x="812" y="2091">and friendly</text>
    <text class="value-text" x="812" y="2103">environment.</text>

    <text class="value-title" x="812" y="2154">BE</text>
    <text class="value-title" x="812" y="2171">POSITIVE</text>
    <text class="value-kicker" x="812" y="2186">SMILE</text>
    <text class="value-text" x="812" y="2198">We are solutions focused and</text>
    <text class="value-text" x="812" y="2211">encourage a positive attitude</text>
    <text class="value-text" x="812" y="2223">turning a negative into a</text>
    <text class="value-text" x="812" y="2235">positive.</text>
  </g>
</svg>
</body>
</html>
```